Stationery (Business Cards, Letterheads & Envelopes)

Require stationery design which includes the following items as a minimum.

- Business card design
- Letterhead
- Envelopes

Details for business card:
Logo: Main logo is called "tovell interiors square gold" but you may make use of whichever logo works best.
Tagline: Exquisite Furniture & Furnishings
Name: Mirren Oskaby
Title: Interior Stylist
Mobile: 0427 318 942
PH: 03 9512 3470
Email: mirren@tovell-interiors.com.au

Industry/Entity Type

Business

```html
<!DOCTYPE html>
<html lang="en">
<head>
<meta charset="utf-8">
<title>Tovell Interiors — Stationery</title>
<link rel="stylesheet" href="https://fonts.googleapis.com/css2?family=Cinzel:wght@400;500&family=Open+Sans:wght@400;600&display=swap">
<style>
  :root {
    --backdrop: #939498;
    --ink: #141414;
    --paper: #f3f3f3;
    --gold: #c9a86a;
    --mark-faint: #e8e9eb;
    --footer-text: #d8d8d8;
    --muted: #5a5a5a;
  }
  * { margin: 0; padding: 0; box-sizing: border-box; }
  html, body { width: 1200px; height: 606px; overflow: hidden; }
  body { background: var(--backdrop); position: relative; font-family: "Open Sans", Arial, sans-serif; }

  .sheet { position: absolute; }
  .folder { left: 48px; top: 46px; width: 356px; height: 504px; background: var(--ink); }
  .letterhead { left: 433px; top: 49px; width: 357px; height: 504px; background: var(--paper); }
  .envelope { left: 812px; width: 297px; height: 148px; background: var(--paper); overflow: hidden; }
  .envelope--flap { top: 49px; }
  .envelope--plain { top: 212px; }
  .envelope--banded { top: 375px; }

  .brand { position: absolute; text-align: center; font-family: "Cinzel", "Times New Roman", serif; font-weight: 400; color: var(--ink); transform: translateX(-50%); }
  .brand__square { display: block; margin: 0 auto; border: 1.5px solid currentColor; }
  .brand__name { display: block; line-height: 1; letter-spacing: 0.06em; white-space: nowrap; }
  .brand__sub { display: block; line-height: 1; letter-spacing: 0.32em; white-space: nowrap; font-weight: 500; }

  .folder .brand { left: 178px; top: 200px; color: var(--gold); }
  .folder .brand__square { width: 26px; height: 26px; margin-bottom: 24px; }
  .folder .brand__name { font-size: 30px; }
  .folder .brand__sub { font-size: 11px; margin-top: 8px; }

  .letterhead .brand { left: 178px; top: 26px; }
  .letterhead .brand__square { width: 22px; height: 22px; margin-bottom: 22px; }
  .letterhead .brand__name { font-size: 24px; }
  .letterhead .brand__sub { font-size: 9px; margin-top: 5px; }

  .envelope .brand { left: 55px; }
  .envelope .brand__square { width: 16px; height: 16px; margin-bottom: 10px; }
  .envelope .brand__name { font-size: 16px; }
  .envelope .brand__sub { font-size: 6.5px; margin-top: 3px; }
  .envelope--plain .brand, .envelope--banded .brand { top: 17px; }

  .watermark { position: absolute; background: var(--mark-faint); opacity: 0.5; border-radius: 50%; }
  .letterhead .watermark { left: 62px; top: 170px; width: 230px; height: 230px; }
  .envelope--banded .watermark { left: 148px; top: 8px; width: 128px; height: 128px; }

  .letterhead__footer { position: absolute; left: 0; bottom: 0; width: 100%; height: 20px; background: var(--ink); display: flex; justify-content: center; align-items: center; gap: 16px; font-size: 7.5px; color: var(--footer-text); }
  .letterhead__footer .label { color: var(--gold); margin-right: 3px; }

  .envelope__flap { position: absolute; left: 0; top: 0; }
  .envelope__seal { position: absolute; left: 142px; top: 10px; width: 13px; height: 13px; border: 1.5px solid var(--gold); }
  .envelope__band { position: absolute; left: 0; bottom: 0; width: 100%; height: 12px; background: var(--ink); }

  .business-card { left: 121px; top: 410px; width: 210px; height: 120px; background: var(--paper); box-shadow: 0 3px 8px rgba(0,0,0,0.45); overflow: hidden; }
  .card__name { position: absolute; left: 16px; top: 15px; font-family: "Cinzel", "Times New Roman", serif; font-size: 13px; line-height: 1; letter-spacing: 0.05em; color: var(--ink); white-space: nowrap; }
  .card__title { position: absolute; left: 16px; top: 33px; font-size: 7.5px; line-height: 1; letter-spacing: 0.2em; text-transform: uppercase; color: var(--gold); font-weight: 600; white-space: nowrap; }
  .card__contacts { position: absolute; left: 16px; top: 52px; list-style: none; font-size: 7.5px; line-height: 12px; color: var(--muted); white-space: nowrap; }
  .card__contacts .label { color: var(--gold); margin-right: 3px; font-weight: 600; }
  .card__tagline { position: absolute; left: 0; bottom: 0; width: 100%; height: 20px; background: var(--ink); color: var(--gold); font-family: "Cinzel", "Times New Roman", serif; font-size: 7.5px; letter-spacing: 0.14em; display: flex; align-items: center; justify-content: center; white-space: nowrap; }
</style>
</head>
<body>

  <section class="sheet folder" aria-label="Presentation folder">
    <div class="brand">
      <span class="brand__square"></span>
      <span class="brand__name">TOVELL</span>
      <span class="brand__sub">INTERIORS</span>
    </div>
  </section>

  <section class="sheet business-card" aria-label="Business card">
    <p class="card__name">Mirren Oskaby</p>
    <p class="card__title">Interior Stylist</p>
    <ul class="card__contacts">
      <li><span class="label">M:</span>0427 318 942</li>
      <li><span class="label">P:</span>03 9512 3470</li>
      <li><span class="label">E:</span>mirren@tovell-interiors.com.au</li>
    </ul>
    <p class="card__tagline">Exquisite Furniture &amp; Furnishings</p>
  </section>

  <section class="sheet letterhead" aria-label="Letterhead">
    <div class="brand">
      <span class="brand__square"></span>
      <span class="brand__name">TOVELL</span>
      <span class="brand__sub">INTERIORS</span>
    </div>
    <div class="watermark" role="img" aria-label="Faint decorative ornament background"></div>
    <footer class="letterhead__footer">
      <span><span class="label">M:</span>0427 318 942</span>
      <span><span class="label">P:</span>03 9512 3470</span>
      <span><span class="label">E:</span>mirren@tovell-interiors.com.au</span>
    </footer>
  </section>

  <section class="sheet envelope envelope--flap" aria-label="Envelope back with flap">
    <svg class="envelope__flap" width="297" height="40" viewBox="0 0 297 40" aria-hidden="true">
      <polygon points="0,0 297,0 297,9 162,38 135,38 0,9" fill="#141414"/>
    </svg>
    <span class="envelope__seal"></span>
  </section>

  <section class="sheet envelope envelope--plain" aria-label="Envelope front">
    <div class="brand">
      <span class="brand__square"></span>
      <span class="brand__name">TOVELL</span>
      <span class="brand__sub">INTERIORS</span>
    </div>
  </section>

  <section class="sheet envelope envelope--banded" aria-label="Envelope front with band">
    <div class="brand">
      <span class="brand__square"></span>
      <span class="brand__name">TOVELL</span>
      <span class="brand__sub">INTERIORS</span>
    </div>
    <div class="watermark" role="img" aria-label="Faint decorative ornament background"></div>
    <div class="envelope__band"></div>
  </section>

</body>
</html>
```